Online retail store selling a multitude of product categories needs a BigCommerce website

We need a website for our online store. We sell over the counter products such as allergy medicine, antacids, and nutritional supplements on several large market places. We want to have a website that can provide our customers with the ease of navigation and quick access to find the products they are searching for, as well as other products, related to their category. The site should have a modern design that fits our products.

Target Market(s)

Consumer of health, household and beauty products.

Font styles to use
Serif
Sans Serif

Colors

Designer to choose colors to be used in the design.

Requirements
Must have
• • Homepage
• • Shop page - in the shop page there should be our product categories
• • Our Operation
• • Contact Us
Nice to have
• I want the site to be organized and well structured.
Should not have
• Not too busy or overstimulating

```html
<!DOCTYPE html>
<html lang="en">
<head>
<meta charset="utf-8">
<title>Pellham Health</title>
<link href="https://fonts.googleapis.com/css2?family=Lato:wght@400;700;900&display=swap" rel="stylesheet">
<style>
:root{
  --blue:#1b5eae;
  --blue-dark:#174f94;
  --green:#61ab4a;
  --green-card:#5ea832;
  --ink:#333333;
  --muted:#555555;
  --panel:#f4f4f4;
  --line:#e2e2e2;
  --white:#ffffff;
}
*{box-sizing:border-box;margin:0;padding:0}
html,body{width:1200px;height:2200px;overflow:hidden;background:var(--white);font-family:'Lato',sans-serif;color:var(--ink)}
.page{position:relative;width:1200px;height:2200px}
.sidebar{position:absolute;left:0;top:0;width:317px;height:2200px;background:var(--blue);color:var(--white)}
.brand{position:absolute;left:28px;top:56px;display:flex;align-items:center;gap:10px;font-weight:900;font-size:27px;letter-spacing:.5px}
.brand-mark{width:22px;height:22px;border-radius:50%;background:var(--white)}
.nav{position:absolute;left:75px;top:167px;width:242px;list-style:none}
.nav li{height:45px;line-height:38px;text-align:center;font-weight:700;font-size:15px;letter-spacing:.3px;width:167px}
.nav li.active{background:var(--green);width:242px;text-align:left;padding-left:63px}
.currency{position:absolute;left:95px;top:444px;width:127px;height:45px;border:1px solid var(--white);font-size:12px;padding:0 18px;display:flex;align-items:center;justify-content:space-between}
.side-links{position:absolute;left:75px;top:518px;width:167px;list-style:none}
.side-links li{height:45px;line-height:28px;text-align:center;font-weight:700;font-size:15px}
.social{position:absolute;left:64px;top:2024px;display:flex;gap:18px}
.social span{width:20px;height:20px;border-radius:50%;background:var(--white)}
.copyright{position:absolute;left:0;top:2068px;width:317px;text-align:center;font-size:13.5px;line-height:21px;letter-spacing:.3px}
.payments{position:absolute;left:62px;top:2139px;display:flex;gap:12px}
.payments span{width:29px;height:19px;border-radius:3px;background:var(--white)}
.topbar{position:absolute;left:317px;top:0;width:883px;height:92px;font-size:13px;letter-spacing:.5px;color:var(--muted)}
.topbar .search{position:absolute;left:23px;top:40px;display:flex;gap:14px;align-items:center}
.topbar .account{position:absolute;left:649px;top:40px;display:flex;gap:8px;align-items:center}
.topbar .cart{position:absolute;left:768px;top:40px;display:flex;gap:8px;align-items:center}
.promo{position:absolute;left:317px;top:92px;width:883px;height:75px;background:var(--green);color:var(--white);font-size:16px;text-align:center;line-height:75px;letter-spacing:.2px}
.hero{position:absolute;left:317px;top:167px;width:883px;height:463px;background:linear-gradient(160deg,#e9d5cb 0%,#dcb8a6 45%,#c99684 75%,#a6715a 100%)}
.hero-card{position:absolute;left:209px;top:128px;width:477px;height:208px;background:rgba(255,255,255,.93);text-align:center}
.hero-card h1{font-size:44px;font-weight:700;margin-top:22px;color:#2b2b2b}
.hero-card p{font-size:19px;line-height:28px;margin-top:6px;color:#3a3a3a}
.btn-outline-green{display:inline-block;margin-top:14px;width:148px;height:45px;line-height:43px;border:1.5px solid var(--green);color:var(--green);font-weight:700;font-size:15px}
.arrow{position:absolute;top:206px;width:53px;height:52px;background:var(--blue);display:flex;align-items:center;justify-content:center}
.arrow.prev{left:181px}.arrow.next{left:662px}
.section-title{position:absolute;left:317px;width:883px;text-align:center;font-size:30px;font-weight:700;color:#333}
.products{position:absolute;left:317px;top:725px;width:883px;display:grid;grid-template-columns:repeat(3,1fr);gap:2px 2px;background:var(--white)}
.product{height:335px;background:var(--panel);position:relative}
.product-photo{position:absolute;left:50%;top:28px;transform:translateX(-50%);width:160px;height:200px;border-radius:6px}
.product-label{position:absolute;left:24px;right:24px;bottom:0;height:86px;background:var(--green-card);color:var(--white);text-align:center;padding-top:20px}
.product-label .name{font-size:18px;font-weight:700;letter-spacing:.3px}
.product-label .price{font-size:17px;font-weight:700;margin-top:6px}
.product-label s{margin-right:20px}
.posts{position:absolute;left:317px;top:1514px;width:883px;height:332px;display:grid;grid-template-columns:293px 297px 293px;border-top:1px solid var(--line)}
.post{border-right:1px solid var(--line);text-align:center;padding-top:78px}
.post .date{color:var(--blue);font-weight:700;font-size:16px;letter-spacing:.3px}
.post p{font-size:19px;line-height:28px;color:#444;margin:8px 22px 0}
.btn-outline-blue{display:inline-block;margin-top:30px;width:148px;height:45px;line-height:43px;border:1.5px solid var(--blue);color:var(--blue);font-weight:700;font-size:16px}
.newsletter{position:absolute;left:317px;top:1846px;width:883px;height:269px;background:var(--panel)}
.newsletter h2{position:absolute;left:0;width:840px;top:64px;text-align:center;font-size:30px;font-weight:700}
.email{position:absolute;left:186px;top:134px;width:333px;height:51px;background:var(--white);border:1px solid #d8d8d8;font-size:12.5px;color:#555;padding-left:14px;line-height:49px}
.subscribe{position:absolute;left:532px;top:134px;width:167px;height:51px;background:var(--blue);color:var(--white);font-weight:700;font-size:13px;text-align:center;line-height:51px;letter-spacing:.3px}
.footer-bar{position:absolute;left:317px;top:2115px;width:883px;height:85px;border-top:1px solid var(--line);font-size:13.5px;color:#444;letter-spacing:.3px}
.footer-bar .links{position:absolute;left:322px;top:42px;display:flex;gap:42px}
.footer-bar .count{position:absolute;right:12px;top:42px;color:#222}
</style>
</head>
<body>
<div class="page">
  <aside class="sidebar">
    <div class="brand"><span class="brand-mark"></span>PELLHAM HEALTH</div>
    <ul class="nav">
      <li class="active">SHOP</li>
      <li>ABOUT</li>
      <li>PRODUCTS</li>
      <li>CONTACT</li>
      <li>RETURNS</li>
      <li>FAQ</li>
    </ul>
    <div class="currency">CAD
      <svg width="8" height="12" viewBox="0 0 8 12"><path d="M4 0L8 5H0zM4 12L0 7h8z" fill="#fff"/></svg>
    </div>
    <ul class="side-links">
      <li>WISHLIST <svg width="16" height="14" viewBox="0 0 16 14" style="vertical-align:-2px;margin-left:6px"><path d="M8 14L1.5 7.5A4 4 0 0 1 8 2.5a4 4 0 0 1 6.5 5z" fill="#fff"/></svg></li>
      <li>GIFT CARDS</li>
    </ul>
    <div class="social" aria-label="Social links"><span></span><span></span><span></span><span></span><span></span></div>
    <div class="copyright">Copyright © 2019 CompanyName<br>All Rights Reserved</div>
    <div class="payments" aria-label="Accepted payments"><span></span><span></span><span></span><span></span><span></span></div>
  </aside>

  <header class="topbar">
    <div class="search">SEARCH
      <svg width="13" height="13" viewBox="0 0 13 13"><circle cx="5.5" cy="5.5" r="4" fill="none" stroke="#555" stroke-width="2"/><path d="M8.5 8.5L12 12" stroke="#555" stroke-width="2"/></svg>
    </div>
    <div class="account">ACCOUNT
      <svg width="12" height="13" viewBox="0 0 12 13"><circle cx="6" cy="3.5" r="3.2" fill="#555"/><path d="M0 13c0-4 2.5-5.5 6-5.5S12 9 12 13z" fill="#555"/></svg>
    </div>
    <div class="cart">CART
      <svg width="13" height="12" viewBox="0 0 13 12"><path d="M0 1h2.5l2 7h7l1.5-5H4" fill="none" stroke="#555" stroke-width="1.6"/><circle cx="5" cy="10.5" r="1.2" fill="#555"/><circle cx="10.5" cy="10.5" r="1.2" fill="#555"/></svg>
    </div>
  </header>

  <div class="promo">Use this banner to inform your customers about special news and promotions!</div>

  <section class="hero">
    <div role="img" aria-label="Photo of a woman using a nasal spray" style="position:absolute;inset:0"></div>
    <div class="hero-card">
      <h1>Pellham Health</h1>
      <p>Curabitur cursus, dui sit amet blandit lacinia,<br>tellus libero lobortis ante.</p>
      <span class="btn-outline-green">SHOP NOW</span>
    </div>
    <div class="arrow prev"><svg width="12" height="18" viewBox="0 0 12 18"><path d="M10 2L3 9l7 7" fill="none" stroke="#fff" stroke-width="3"/></svg></div>
    <div class="arrow next"><svg width="12" height="18" viewBox="0 0 12 18"><path d="M2 2l7 7-7 7" fill="none" stroke="#fff" stroke-width="3"/></svg></div>
  </section>

  <h2 class="section-title" style="top:662px">Featured Products</h2>
  <section class="products">
    <div class="product"><div class="product-photo" role="img" aria-label="Baby probiotic drops box and bottle" style="background:linear-gradient(135deg,#7b3c8e,#e8e1ec)"></div><div class="product-label"><div class="name">PRODUCT NAME</div><div class="price"><s>$16.00</s>$13.00</div></div></div>
    <div class="product"><div class="product-photo" role="img" aria-label="Night dental guard kit with case" style="background:linear-gradient(135deg,#dfe4ea,#2a56a0)"></div><div class="product-label"><div class="name">PRODUCT NAME</div><div class="price"><s>$16.00</s>$13.00</div></div></div>
    <div class="product"><div class="product-photo" role="img" aria-label="Dental guard retail box" style="background:linear-gradient(180deg,#1f6fc4,#e9eef4)"></div><div class="product-label"><div class="name">PRODUCT NAME</div><div class="price"><s>$16.00</s>$13.00</div></div></div>
    <div class="product"><div class="product-photo" role="img" aria-label="Heartburn relief capsule box" style="width:240px;height:170px;top:52px;background:linear-gradient(90deg,#1d3f9c,#e85a24)"></div><div class="product-label"><div class="name">PRODUCT NAME</div><div class="price"><s>$16.00</s>$13.00</div></div></div>
    <div class="product"><div class="product-photo" role="img" aria-label="Cold sore cream pump pack" style="width:190px;height:200px;border-radius:45%;background:radial-gradient(#3f7ed6,#1b4d9c 70%,#d9dde4)"></div><div class="product-label"><div class="name">PRODUCT NAME</div><div class="price"><s>$16.00</s>$13.00</div></div></div>
    <div class="product"><div class="product-photo" role="img" aria-label="Ovulation test kit box" style="width:95px;height:200px;background:linear-gradient(180deg,#f3d23a 0%,#5a3c9c 20%,#6f8fd0 100%)"></div><div class="product-label"><div class="name">PRODUCT NAME</div><div class="price"><s>$16.00</s>$13.00</div></div></div>
  </section>

  <h2 class="section-title" style="top:1455px">Recent Posts</h2>
  <section class="posts">
    <article class="post"><div class="date">SEP 20 ,2109</div><p>Curabitur cursus, dui sit amet blandit lacinia, tellus libero lobortis ante.</p><span class="btn-outline-blue">READ MORE</span></article>
    <article class="post"><div class="date">SEP 20 ,2109</div><p>Curabitur cursus, dui sit amet blandit lacinia, tellus libero lobortis ante.</p><span class="btn-outline-blue">READ MORE</span></article>
    <article class="post"><div class="date">SEP 20 ,2109</div><p>Curabitur cursus, dui sit amet blandit lacinia, tellus libero lobortis ante.</p><span class="btn-outline-blue">READ MORE</span></article>
  </section>

  <section class="newsletter">
    <h2>Join our Newsletter</h2>
    <div class="email">Enter Email Address</div>
    <div class="subscribe">SUBSCRIBE NOW</div>
  </section>

  <footer class="footer-bar">
    <div class="links"><span>NEW ARRIVALS</span><span>SALE</span><span>SHOP</span></div>
    <div class="count">X10</div>
  </footer>
</div>
</body>
</html>
```